Website for AV installation with booking system and e-commerce

Company: Velqora
Tag Line: Audio Visual and Security System Installations
We need a website for an AV company based in Sydney Australia. We specialise in Audio Visual, CCTV (security cameras), and Data Cabling.
The purpose of the website is that customers book their installation online with a live booking system.
We are looking for the following:
- Creative and modern design
- easy to use - keep in mind that the user who will book will have little knowledge in technology.
- clean and organised
- colours to work in well with our logo we also like royal to navy blue, but we are open to other suggested what works well with our logo.
We want customers to be able to add products needed for their installation ie when booking to wall mount their TV they can choose to add a TV bracket and cables to the cart and vise-versa buy a bracket or cables and add to cart the installation.
Tabs to be included:
About us
Gallery
Contact Us
Home
Services (there are three services that we offer - Residential, Corporate and Retail)
Products
Book Online/Cart (checkout)
Temporary website checkout: www.velqora.com.au, please note this is very basic and we do not want a copy of this. This is purely to give you an idea of our company.
Good Luck!
Updates
Target Market(s)
home owners/renters, business owners, archiects/designers, builders
Industry/Entity Type
E-Commerce
Look and feel

```html
<!DOCTYPE html>
<html lang="en">
<head>
<meta charset="utf-8">
<title>Velqora – Audio Visual and Security System Installations</title>
<link href="https://fonts.googleapis.com/css2?family=PT+Sans:wght@400;700&family=Ubuntu:wght@400;500;700&family=Yanone+Kaffeesatz:wght@400;600;700&display=swap" rel="stylesheet">
<style>
:root{
  --dark:#2b2e33;
  --dark-2:#24272b;
  --red:#d2131b;
  --red-dark:#9c0a0f;
  --white:#ffffff;
  --paper:#efefef;
  --ink:#1b1b1b;
  --muted:#c9cbce;
  --field:#efefef;
  --field-line:#cfcfcf;
  --link-red:#c8141a;
}
*{margin:0;padding:0;box-sizing:border-box}
html,body{width:1128px;height:1200px;overflow:hidden}
body{position:relative;background:var(--dark);font-family:"Ubuntu",sans-serif;color:var(--ink)}
.abs{position:absolute}

/* header */
.top-band{left:0;top:0;width:1128px;height:524px;background:linear-gradient(#2e3136,#26292d)}
.red-rule{left:0;top:66px;width:1128px;height:11px;background:linear-gradient(var(--red),var(--red-dark));border-top:1px solid #ff4a4f}
.logo-tab{left:169px;top:0;width:234px;height:88px}
.logo-name{left:169px;top:20px;width:234px;text-align:center;font-family:"Ubuntu",sans-serif;font-weight:700;font-size:34px;color:var(--red);letter-spacing:1px}
.nav{left:541px;top:26px;display:flex;gap:10px;font-family:"Ubuntu",sans-serif;font-size:12px;color:var(--muted)}
.nav .current{color:var(--white);font-weight:500}
.booking{left:868px;top:23px;width:90px;height:21px;background:linear-gradient(#f4f4f4,#cfcfcf);border-radius:2px;font-size:12px;font-weight:500;color:#222;text-align:center;line-height:21px}
.cart{left:770px;top:89px;font-size:9.5px;color:var(--white);display:flex;align-items:center;gap:8px}
.cards{left:889px;top:91px;display:flex;gap:3px}
.cards span{width:14px;height:10px;border-radius:1px}

/* hero */
.hero{left:169px;top:114px;width:790px;height:310px;border-radius:4px;overflow:hidden;background:linear-gradient(100deg,#ffffff 0%,#fbf1e4 35%,#f3c9a0 55%,#d8342a 75%,#b8181c 100%)}
.hero-title{left:206px;top:186px;font-family:"PT Sans",sans-serif;font-size:48px;line-height:54px;color:#0d0d0d;letter-spacing:-1px}
.hero-title b{font-weight:700}

/* service buttons */
.service{top:444px;width:244px;height:52px;background:linear-gradient(#e01e25,#a80c10);border:1px solid #ef3b40;border-radius:3px;box-shadow:0 6px 8px rgba(0,0,0,.45);color:var(--white)}
.service h3{position:absolute;left:46px;top:7px;font-family:"PT Sans",sans-serif;font-size:19px;font-weight:700}
.service p{position:absolute;left:47px;top:31px;font-size:10.5px}
.service .icon{position:absolute;left:8px;top:13px}
.corporate h3,.corporate p{left:38px}
.dark-rule{left:0;top:524px;width:1128px;height:9px;background:linear-gradient(#000,#3a3d42 60%,#111)}

/* light section */
.light{left:0;top:533px;width:1128px;height:481px;background:var(--paper)}
.panel{left:170px;top:550px;width:788px;height:449px;background:var(--white);box-shadow:0 0 3px rgba(0,0,0,.15)}
.feature h4{font-family:"Yanone Kaffeesatz",sans-serif;font-weight:700;font-size:21px;line-height:20px;color:#111}
.feature-text{font-size:10px;line-height:15.5px;color:#222;width:200px}
.feature-icon{border-radius:6px}
.divider-v{left:646px;top:568px;width:1px;height:226px;background:#e2e2e2}

.enquiry-title{left:669px;top:566px;font-family:"Yanone Kaffeesatz",sans-serif;font-size:22px;color:#111}
.field{left:668px;width:266px;background:var(--field);border:1px solid var(--field-line);font-size:10px;color:#888;padding:9px 7px}
.submit{left:849px;top:778px;width:84px;height:29px;background:linear-gradient(#d6151c,#9c0a0f);border-radius:2px;color:var(--white);font-family:"PT Sans",sans-serif;font-weight:700;font-size:15px;text-align:center;line-height:29px}
.hr{left:185px;top:811px;width:756px;height:1px;background:#e8e8e8}

.welcome-title{left:189px;top:835px;font-family:"Yanone Kaffeesatz",sans-serif;font-size:19px;color:#111}
.welcome-text{left:192px;top:871px;width:494px;font-size:10px;line-height:15.3px;color:#111}
.welcome-text p+p{margin-top:15.3px}

.testimonials{left:708px;top:827px;width:241px;height:163px;background:#f5f5f5;border:1px solid #e3e3e3}
.testimonials h4{position:absolute;left:22px;top:13px;font-family:"Yanone Kaffeesatz",sans-serif;font-weight:400;font-size:19px;color:#111}
.testimonials .date{position:absolute;left:21px;top:45px;font-size:10.5px}
.testimonials .quote{position:absolute;left:21px;top:62px;width:212px;font-size:9px;line-height:15px}
.testimonials .author{position:absolute;left:21px;top:107px;font-size:10.5px;font-weight:500}
.testimonials a{position:absolute;left:21px;top:131px;font-size:9px;color:var(--link-red)}

/* footer */
.footer{left:0;top:1014px;width:1128px;height:186px;background:var(--dark-2)}
.foot-col h5{font-family:"Ubuntu",sans-serif;font-weight:400;font-size:14.5px;color:var(--white);margin-bottom:14px}
.foot-col li{list-style:none;font-size:10px;color:var(--muted);line-height:18.5px}
.foot-col p{font-size:10px;color:var(--muted);line-height:18.7px;width:160px}
.foot-div{top:1032px;width:1px;height:150px;background:#1a1c1f;box-shadow:1px 0 0 #33363b}
.social{display:flex;align-items:center;gap:20px;font-size:10px;color:var(--muted);margin-bottom:14px}
.social span{width:19px;height:19px;border-radius:2px;background:#4a9ad6}
</style>
</head>
<body>

<div class="abs top-band"></div>
<div class="abs red-rule"></div>

<svg class="abs logo-tab" viewBox="0 0 234 88" aria-hidden="true">
  <defs><linearGradient id="tabfill" x1="0" y1="0" x2="0" y2="1"><stop offset="0" stop-color="#ffffff"/><stop offset="1" stop-color="#e4e4e4"/></linearGradient></defs>
  <path d="M0 0H234V71L117 88L0 71Z" fill="url(#tabfill)"/>
</svg>
<div class="abs logo-name">Velqora</div>

<nav class="abs nav">
  <span class="current">HOME</span><span>About us</span><span>Gallery</span><span>Services</span><span>Products</span><span>Contact Us</span>
</nav>
<div class="abs booking">Booking Online</div>

<div class="abs cart">
  <svg width="15" height="12" viewBox="0 0 15 12" aria-hidden="true"><path d="M0 1h3l2 7h8l2-5H4" fill="none" stroke="#fff" stroke-width="1.2"/><circle cx="6" cy="10.5" r="1.2" fill="#fff"/><circle cx="12" cy="10.5" r="1.2" fill="#fff"/></svg>
  <span>0 items in your cart</span>
</div>
<div class="abs cards" aria-label="Accepted payment cards">
  <span style="background:#1d3e8c"></span><span style="background:#e3a11a"></span><span style="background:#e8e8e8"></span><span style="background:#1a4fa0"></span>
</div>

<div class="abs hero" role="img" aria-label="Close-up photograph of red audio-visual RCA cable connectors"></div>
<div class="abs hero-title"><b>Audio Visual</b> and<br><b>Security System</b><br>Installations</div>

<div class="abs service residential" style="left:169px">
  <svg class="icon" width="32" height="28" viewBox="0 0 32 28" aria-hidden="true"><path d="M16 2L1 15h4v12h8v-8h6v8h8V15h4z" fill="#111"/></svg>
  <h3>Residential</h3><p>Lorem Ipsum is simply dummy text of</p>
</div>
<div class="abs service corporate" style="left:442px">
  <svg class="icon" width="22" height="26" viewBox="0 0 22 26" aria-hidden="true"><circle cx="9" cy="9" r="7" fill="none" stroke="#111" stroke-width="2"/><rect x="7" y="8" width="5" height="14" rx="2" fill="#111"/><rect x="7" y="15" width="12" height="9" rx="3" fill="#111"/></svg>
  <h3>Corporate</h3><p>Lorem Ipsum is simply dummy text of</p>
</div>
<div class="abs service retail" style="left:715px">
  <svg class="icon" width="26" height="26" viewBox="0 0 26 26" aria-hidden="true"><rect x="1" y="1" width="24" height="24" rx="3" fill="#111"/><rect x="5" y="9" width="6" height="12" fill="#fff"/><rect x="14" y="7" width="7" height="14" fill="#fff"/></svg>
  <h3>Retail</h3><p>Lorem Ipsum is simply dummy text of</p>
</div>

<div class="abs dark-rule"></div>
<div class="abs light"></div>
<div class="abs panel"></div>

<!-- features -->
<svg class="abs" style="left:193px;top:586px" width="40" height="40" viewBox="0 0 40 40" aria-hidden="true">
  <circle cx="20" cy="21" r="18" fill="#d92c2c"/>
  <path d="M20 21L20 3A18 18 0 0 1 38 21Z" fill="#f2b01e"/>
  <path d="M20 21L38 21A18 18 0 0 1 24 38.5Z" fill="#4fa83a"/>
  <path d="M20 21L24 38.5A18 18 0 0 1 5 31Z" fill="#2f7fc8"/>
</svg>
<div class="abs feature" style="left:242px;top:587px"><h4>Increase Your<br>Profit</h4></div>
<div class="abs feature-text" style="left:186px;top:630px">Plusieurs variations de Lorem Ipsum être trouvées ici ou là.</div>

<div class="abs feature-icon" style="left:445px;top:584px;width:40px;height:40px;background:radial-gradient(circle at 40% 40%,#fff6a0,#f2c419 60%,#bfbfbf 61%)" role="img" aria-label="Light bulb icon"></div>
<div class="abs feature" style="left:497px;top:587px"><h4>Your perfect<br>solution</h4></div>
<div class="abs feature-text" style="left:442px;top:630px">Plusieurs variations de Lorem Ipsum être trouvées ici ou là.</div>

<div class="abs feature-icon" style="left:194px;top:691px;width:38px;height:35px;background:linear-gradient(#2c62c4,#173a7a)" role="img" aria-label="Television set icon"></div>
<div class="abs feature" style="left:242px;top:709px"><h4>TV bracket</h4></div>
<div class="abs feature-text" style="left:186px;top:754px">Plusieurs variations de Lorem Ipsum être trouvées ici ou là.</div>

<div class="abs feature-icon" style="left:450px;top:706px;width:34px;height:40px;background:linear-gradient(#e0b07f,#8e949c)" role="img" aria-label="Installer figure icon"></div>
<div class="abs feature" style="left:497px;top:709px"><h4>Easily<br>Installation</h4></div>
<div class="abs feature-text" style="left:442px;top:754px">Plusieurs variations de Lorem Ipsum être trouvées ici ou là.</div>

<div class="abs divider-v"></div>

<!-- enquiry -->
<div class="abs enquiry-title">Online Enquiry</div>
<div class="abs field" style="top:596px;height:26px;padding-top:7px">Full Name:</div>
<div class="abs field" style="top:630px;height:26px;padding-top:7px">Email:</div>
<div class="abs field" style="top:664px;height:26px;padding-top:7px">Telephone Number:</div>
<div class="abs field" style="top:698px;height:74px">Message:</div>
<div class="abs submit">Submit</div>

<div class="abs hr"></div>

<div class="abs welcome-title">Welcome to Velqora</div>
<div class="abs welcome-text">
  <p>Le Lorem Ipsum est simplement du faux texte employé dans la composition et la mise en page avant impression. Le Lorem Ipsum est le faux texte standard de l'imprimerie depuis les années 1500.</p>
  <p>Quand un peintre anonyme assembla ensemble des morceaux de texte pour réaliser un livre spécimen de polices de texte. Il n'a pas fait que survivre cinq siècles, mais s'est aussi adapté à la bureautique informa-tique, sans que son contenu n'en soit modifiéuand un peintre anonyme assembla ensemble des morceaux de texte pour réaliser un livre spécimen de</p>
</div>

<div class="abs testimonials">
  <h4>Tesimonials</h4>
  <div class="date">22 Oct, 2012</div>
  <div class="quote">Le Lorem Ipsum est simplement du faux texte employé dans la composition et la mise en page avant impression.</div>
  <div class="author">Marlow Pennick</div>
  <a href="#">Read More</a>
</div>

<!-- footer -->
<div class="abs footer"></div>
<div class="abs foot-div" style="left:381px"></div>
<div class="abs foot-div" style="left:566px"></div>
<div class="abs foot-div" style="left:798px"></div>

<div class="abs foot-col" style="left:197px;top:1034px">
  <h5>About Velqora</h5>
  <p>Le Lorem Ipsum est simplement du faux texte employé dans la composition et la mise en page avant impression.</p>
</div>
<div class="abs foot-col" style="left:429px;top:1034px">
  <h5>About Us</h5>
  <ul><li>Home</li><li>Gallery</li><li>Services</li><li>Products</li><li>Contact Us</li></ul>
</div>
<div class="abs foot-col" style="left:620px;top:1034px">
  <h5>Support</h5>
  <ul><li>Support Community</li><li>Getting Started Guide</li></ul>
  <h5 style="margin-top:12px">Video</h5>
  <ul><li>Quick Video Tour Of Brixlo</li></ul>
</div>
<div class="abs foot-col" style="left:841px;top:1034px">
  <h5>Social Media</h5>
  <div class="social">Circlefeed <span></span></div>
  <div class="social">Chirpline <span style="margin-left:7px"></span></div>
</div>

</body>
</html>
```